Riverline Estate Holdings Co.

We need a logo and business card design for a Hong Kong based real estate company, KDT Land. We are want the brand to reflect the owners forward thinking, creative, and trend setting projects, while also reflecting a sense of security and strength. We invest in industrial properties which we convert to co-living or co-working spaces. KDT stands for Greater Bay Area which is the region around southern China including HK, Macau, and 9 other Chinese cities...made up of approx. 68 million people. There are massive infrastructure projects including the bridge to Macau and high-speed rail to SZ and the bridge connecting SZ and Zhongshan.

Target Market(s)

Chinese and western retail investors, as well as institutional investors

Industry/Entity Type

Real Estate Development

Contact Information for Business Card

Owen Tallis
CEO
owen@kdtland-hq.com
M + 852 9416 2057
F + 852 3582 0400
Suite 2207, The Meridale, 41 Larchmont Rd., Central, Hong Kong

Logo Text

kdt land (company name) lifestyle property development (underneath)

Colors

Designer to choose colors to be used in the design.

Requirements
Must have
• Details listed above. One side should include the logo and company name...kdt land in modern, hip styling with "lifestyle property development"
Nice to have
• Could be a Black card, with metallic purple "kdt" and white "land"...but open great design ideas
Should not have
• boring and traditional layout

```html
<!DOCTYPE html>
<html lang="en">
<head>
<meta charset="utf-8">
<title>KDT Land – Business Card</title>
<link href="https://fonts.googleapis.com/css2?family=Audiowide&family=Open+Sans:wght@400;600&family=Oswald:wght@500&display=swap" rel="stylesheet">
<style>
  :root {
    --stage: #2b2624;
    --card: #121212;
    --gold: #e0a818;
    --silver: #c9c9c9;
    --grey: #9a9a9a;
    --white: #f1f1f1;
    --rule: #4a4a4a;
  }
  * { box-sizing: border-box; margin: 0; padding: 0; }
  html, body { width: 1200px; height: 844px; overflow: hidden; }
  body {
    background: var(--stage);
    position: relative;
    font-family: "Open Sans", sans-serif;
  }
  .card {
    position: absolute;
    width: 520px;
    height: 300px;
    background: var(--card);
    box-shadow: 0 10px 30px rgba(0,0,0,.45);
    overflow: hidden;
  }
  .card--front { left: 50px; top: 272px; }
  .card--back  { left: 630px; top: 272px; }

  .brand { position: absolute; text-align: center; }
  .brand__name {
    font-family: "Audiowide", sans-serif;
    line-height: 1;
    letter-spacing: 1px;
    white-space: nowrap;
  }
  .brand__tagline {
    font-family: "Oswald", sans-serif;
    font-weight: 500;
    letter-spacing: .6px;
    text-transform: uppercase;
    color: var(--grey);
    margin-top: 12px;
    padding-top: 8px;
    border-top: 1px solid var(--rule);
    white-space: nowrap;
  }
  .card--front .brand { left: 28px; top: 110px; width: 226px; }
  .card--front .brand__name { color: var(--gold); font-size: 34px; }
  .card--front .brand__tagline { font-size: 12px; }
  .card--back .brand { left: 0; right: 0; top: 98px; margin: 0 auto; width: 330px; }
  .card--back .brand__name { color: var(--silver); font-size: 50px; }
  .card--back .brand__tagline { color: var(--silver); font-size: 14px; }

  .divider {
    position: absolute;
    left: 282px; top: 40px;
    width: 1px; height: 220px;
    background: var(--rule);
  }

  .contact { position: absolute; left: 306px; top: 58px; color: var(--white); }
  .contact__name {
    font-family: "Audiowide", sans-serif;
    color: var(--gold);
    font-size: 17px;
    font-weight: 400;
    letter-spacing: .5px;
    text-transform: uppercase;
  }
  .contact__role { font-size: 12px; color: var(--white); margin: 2px 0 10px; }
  .contact__list { list-style: none; }
  .contact__item {
    display: flex; align-items: center; gap: 7px;
    font-size: 13px; line-height: 19px;
  }
  .contact__item svg { width: 11px; height: 11px; flex: none; }
  .contact__address { font-size: 13px; line-height: 19px; margin-top: 12px; }
</style>
</head>
<body>

  <section class="card card--front" aria-label="Business card, contact side">
    <div class="brand">
      <div class="brand__name">KDT Land</div>
      <div class="brand__tagline">Lifestyle Property Development</div>
    </div>

    <div class="divider"></div>

    <div class="contact">
      <h1 class="contact__name">Owen Tallis</h1>
      <p class="contact__role">CEO</p>
      <ul class="contact__list">
        <li class="contact__item">
          <svg viewBox="0 0 12 12" aria-hidden="true"><rect x="3" y="0.5" width="6" height="11" rx="1" fill="none" stroke="var(--gold)" stroke-width="1.2"/><circle cx="6" cy="9.5" r=".8" fill="var(--gold)"/></svg>
          + 852 9416 2057
        </li>
        <li class="contact__item">
          <svg viewBox="0 0 12 12" aria-hidden="true"><rect x="3" y="0.5" width="6" height="3" fill="var(--gold)"/><rect x="0.5" y="4" width="11" height="5" rx="1" fill="var(--gold)"/><rect x="3" y="8" width="6" height="3.5" fill="var(--gold)"/></svg>
          + 852 3582 0400
        </li>
        <li class="contact__item">
          <svg viewBox="0 0 12 12" aria-hidden="true"><rect x="0.5" y="2" width="11" height="8" fill="var(--gold)"/><path d="M0.5 2 L6 6.5 L11.5 2" fill="none" stroke="var(--card)" stroke-width="1"/></svg>
          owen@kdtland-hq.com
        </li>
      </ul>
      <p class="contact__address">Suite 2207, The Meridale<br>41 Larchmont Rd.,<br>Central, Hong Kong</p>
    </div>
  </section>

  <section class="card card--back" aria-label="Business card, brand side">
    <div class="brand">
      <div class="brand__name">KDT Land</div>
      <div class="brand__tagline">Lifestyle Property Development</div>
    </div>
  </section>

</body>
</html>
```